Ethiopian Coffee Brand "Kelo Mar'isa" needs a Brand Label. *

We need a brand label design to go on our coffee bags. The coffee is Ethiopian Yirgacheffe. The Brand is called " Kelo Mar'isa " In Amharic it is " ሎሜ ዳራ ". We are aiming at a luxury market. We are looking for something that shows the African continent, the cloud forests where the coffee grows or just an image that is quintessentially African and the birthplace of the coffee industry. Ethiopian Coffee is widely considered to be the origin location for coffee. Our coffee bags are going to be either gold or black. The main ideas we want to convey are luxury, history, and gravitas. Our parent company is called Pelwick Trading, we are committed to the environment and protecting endangered species. If there is a way to convey this as well without overly complicating the design then wonderful,if not then no problem.
Coffee Drinkers in N. America who shop on Torvane

```html
<!DOCTYPE html>
<html lang="en">
<head>
<meta charset="utf-8">
<title>Kelo Mar'isa — Ethiopian Yirgacheffe Label</title>
<link rel="stylesheet" href="https://fonts.googleapis.com/css2?family=Fredoka:wght@600&family=Noto+Sans+Ethiopic:wght@500&family=Montserrat:wght@700&family=Questrial&family=Oswald:wght@500;600&display=swap">
<style>
  :root {
    --backdrop: #d9d9d9;
    --bag-black: #141414;
    --bag-shade: #1c1c1c;
    --gold: #e4b22f;
    --gold-deep: #b98a1c;
    --white: #ffffff;
  }
  * { margin: 0; padding: 0; box-sizing: border-box; }
  html, body {
    width: 1200px; height: 1200px; overflow: hidden;
    background: var(--backdrop);
  }
  .canvas { position: relative; width: 1200px; height: 1200px; }
  .label {
    position: absolute; left: 270px; top: 70px;
    width: 660px; height: 1060px;
    background: var(--bag-black);
    color: var(--white);
  }
  .heritage-band {
    position: absolute; left: 0; top: 12px; width: 100%; height: 273px;
    background: linear-gradient(180deg, var(--bag-black) 0%, #2a2210 20%, #5a4415 50%, #2a2210 80%, var(--bag-black) 100%);
  }
  .field-pattern {
    position: absolute; left: 0; top: 285px; width: 100%; height: 775px;
    background: radial-gradient(ellipse at center, var(--bag-shade) 0%, var(--bag-black) 75%);
  }
  .content { position: absolute; left: 0; right: 0; top: 0; text-align: center; }
  .brand-name {
    position: absolute; left: 0; right: 0; top: 350px;
    font-family: "Fredoka", sans-serif; font-weight: 600;
    font-size: 62px; color: var(--gold); letter-spacing: 1px;
  }
  .brand-name-amharic {
    position: absolute; left: 230px; right: 0; top: 425px;
    font-family: "Noto Sans Ethiopic", sans-serif; font-weight: 500;
    font-size: 34px; color: var(--gold); text-align: left; padding-left: 80px;
  }
  .rule {
    position: absolute; left: 105px; width: 450px; height: 2px;
    background: var(--gold);
  }
  .rule.top { top: 510px; }
  .rule.bottom { top: 648px; }
  .origin-title {
    position: absolute; left: 0; right: 0; top: 536px;
    font-family: "Montserrat", sans-serif; font-weight: 700;
    font-size: 32px; color: var(--white);
  }
  .product-type {
    position: absolute; left: 0; right: 0; top: 592px;
    font-family: "Questrial", sans-serif;
    font-size: 33px; color: var(--white); letter-spacing: 0.5px;
  }
  .single-origin {
    position: absolute; left: 0; right: 0; top: 660px;
    font-family: "Oswald", sans-serif; font-weight: 600;
    font-size: 33px; color: var(--gold); letter-spacing: 1px;
  }
  .spec-table {
    position: absolute; left: 105px; top: 712px; width: 450px;
    font-family: "Oswald", sans-serif; font-weight: 500;
    border-top: 2px dashed var(--gold);
  }
  .spec-row {
    display: flex; align-items: center;
    border-bottom: 2px dashed var(--gold);
    height: 58px;
  }
  .spec-key, .spec-value { display: flex; align-items: center; height: 100%; }
  .spec-key { padding-left: 20px; }
  .spec-value { flex: 1; justify-content: center; border-left: 2px dashed var(--gold); height: 60%; }
  .spec-row.process .spec-key { width: 205px; font-size: 25px; }
  .spec-row.process .spec-value { font-size: 25px; }
  .spec-row.altitude .spec-key { width: 185px; font-size: 19px; }
  .spec-row.altitude .spec-value { font-size: 19px; }
  .spec-row.varietal .spec-key { width: 165px; font-size: 19px; }
  .spec-row.varietal .spec-value { font-size: 19px; justify-content: flex-start; padding-left: 30px; }
  .net-weight {
    position: absolute; left: 0; right: 0; top: 910px;
    font-family: "Questrial", sans-serif; font-size: 23px; color: var(--white);
  }
  .net-weight .amount { font-size: 34px; margin: 0 8px; }
</style>
</head>
<body>
<div class="canvas">
  <div class="label">
    <div class="heritage-band" role="img" aria-label="Gold Ethiopian tibeb border band with zigzag lines and cross-lattice motifs"></div>
    <div class="field-pattern" role="img" aria-label="Subtle dark tonal lace pattern covering the black bag"></div>

    <div class="content">
      <h1 class="brand-name">Kelo Mar'isa</h1>
      <p class="brand-name-amharic" lang="am">ሎሜ ዳራ</p>

      <div class="rule top"></div>
      <h2 class="origin-title">Ethiopian Yirgacheffe</h2>
      <p class="product-type">Premium Coffee</p>
      <div class="rule bottom"></div>

      <p class="single-origin">SINGLE ORIGIN</p>

      <div class="spec-table">
        <div class="spec-row process">
          <span class="spec-key">PROCESS</span>
          <span class="spec-value">NATURAL</span>
        </div>
        <div class="spec-row altitude">
          <span class="spec-key">ALTITUDE</span>
          <span class="spec-value">1900 -2200 METERS</span>
        </div>
        <div class="spec-row varietal">
          <span class="spec-key">VARIETAL</span>
          <span class="spec-value">HEIRLOOM</span>
        </div>
      </div>

      <p class="net-weight">Net Wt.<span class="amount">12</span>Ounces</p>
    </div>
  </div>
</div>
</body>
</html>
```